New Business Card Design Project

hello again,
i have an awful year and we were not able to complete our logo plan. we would like to use our #1 logo for business card design process. the primary colors for business card should be white background with orange & black letters. our business is mobil truck cranes. we deliver heavy stuff and unload cargo with crane that is mounted on our trucks.
here is our business card info:
HARBOR LIFT HAULERS, INC.
428 WESTCOTT AVE
MERRICK, NY 11542
OFFICE - 516 487 3091
DIRECT - 1 888 LIFT HAULS
MARK@HLHAULERS.COM
PLEASE also try to get our slogan on card .... "Our Loads Keep Rollin"
lastly please also put "24 hour Knuckleboom Service"
you can call me anytime 24/7 to discuss...my cell # is: 516 759 2036
please also list: Mark Delroy, President
Target Market(s)
Heavy Construction industry
Industry/Entity Type
heavy construction industry
Contact Information for Business Card
24 Hr Knuckleboom Service

```html
<!DOCTYPE html>
<html lang="en">
<head>
<meta charset="utf-8">
<title>Harbor Lift Haulers — Business Card</title>
<link rel="stylesheet" href="https://fonts.googleapis.com/css2?family=Arimo:wght@400;700&display=swap">
<style>
  :root {
    --stage: #2b2b2b;
    --card: #ffffff;
    --orange: #f0380f;
    --ink: #1e1e1e;
    --grey: #4a4a4a;
    --rule: #b5b5b5;
  }
  * { box-sizing: border-box; margin: 0; padding: 0; }
  html, body { width: 1200px; height: 1040px; overflow: hidden; }
  body {
    background: var(--stage);
    font-family: "Arimo", Arial, sans-serif;
    color: var(--ink);
    position: relative;
  }
  .card {
    position: absolute;
    left: 230px;
    width: 740px;
    height: 422px;
    background: var(--card);
    box-shadow: 0 12px 30px rgba(0,0,0,.45);
  }
  .card--front { top: 60px; border-radius: 90px 0 90px 0; }
  .card--back  { top: 552px; border-radius: 0 90px 0 90px; }

  .brand { display: flex; flex-direction: column; align-items: center; }
  .brand__slogan {
    font-size: 17px; font-weight: 700; letter-spacing: 1px;
    color: var(--grey); text-transform: uppercase; margin-bottom: 10px;
  }
  .brand__row { display: flex; align-items: center; gap: 12px; }
  .brand__dot { width: 26px; height: 26px; border-radius: 50%; background: var(--orange); flex: none; }
  .brand__name { font-weight: 700; color: var(--ink); white-space: nowrap; }

  .card--front .brand { position: absolute; left: 0; right: 0; top: 130px; }
  .card--front .brand__name { font-size: 36px; }
  .service {
    position: absolute; left: 0; right: 0; top: 262px;
    text-align: center; color: var(--orange);
    font-size: 21px; letter-spacing: .5px;
  }

  .card--back .brand { position: absolute; left: 30px; width: 360px; top: 150px; }
  .card--back .brand__slogan { font-size: 13px; }
  .card--back .brand__dot { width: 18px; height: 18px; }
  .card--back .brand__name { font-size: 20px; }

  .divider {
    position: absolute; left: 412px; top: 90px; width: 1px; height: 260px; background: var(--rule);
  }
  .contact { position: absolute; left: 440px; top: 108px; }
  .contact__name { color: var(--orange); font-size: 30px; font-weight: 700; line-height: 1; white-space: nowrap; }
  .contact__title { font-size: 19px; color: var(--ink); margin: 4px 0 12px; }
  .contact__list { list-style: none; }
  .contact__item { display: flex; align-items: center; gap: 6px; font-size: 19px; line-height: 25px; white-space: nowrap; }
  .contact__icon {
    width: 20px; height: 20px; border-radius: 50%; background: var(--orange);
    display: flex; align-items: center; justify-content: center; flex: none;
  }
  .contact__icon svg { width: 12px; height: 12px; }
  .contact__hl { color: var(--orange); }
  .contact__address { margin-top: 14px; font-size: 19px; line-height: 24px; }
</style>
</head>
<body>

<section class="card card--front">
  <div class="brand">
    <p class="brand__slogan">Our Loads Keep Rollin</p>
    <div class="brand__row">
      <span class="brand__dot"></span>
      <span class="brand__name">HARBOR LIFT HAULERS, INC.</span>
    </div>
  </div>
  <p class="service">24 HOUR KNUCKLEBOOM SERVICE</p>
</section>

<section class="card card--back">
  <div class="brand">
    <p class="brand__slogan">Our Loads Keep Rollin</p>
    <div class="brand__row">
      <span class="brand__dot"></span>
      <span class="brand__name">HARBOR LIFT HAULERS, INC.</span>
    </div>
  </div>

  <div class="divider"></div>

  <div class="contact">
    <p class="contact__name">MARK DELROY</p>
    <p class="contact__title">President</p>
    <ul class="contact__list">
      <li class="contact__item">
        <span class="contact__icon"><svg viewBox="0 0 12 12"><path d="M2.5 1 L4.5 1 L5 3.5 L3.8 4.3 C4.4 5.8 5.8 7.3 7.5 8 L8.3 6.9 L11 7.4 L11 9.5 C11 10.3 10.3 11 9.5 11 C5 10.7 1.3 7 1 2.5 C1 1.7 1.7 1 2.5 1 Z" fill="#fff"/></svg></span>
        <span class="contact__text">516 487 3091</span>
      </li>
      <li class="contact__item">
        <span class="contact__icon"><svg viewBox="0 0 12 12"><path d="M2.5 1 L4.5 1 L5 3.5 L3.8 4.3 C4.4 5.8 5.8 7.3 7.5 8 L8.3 6.9 L11 7.4 L11 9.5 C11 10.3 10.3 11 9.5 11 C5 10.7 1.3 7 1 2.5 C1 1.7 1.7 1 2.5 1 Z" fill="#fff"/></svg></span>
        <span class="contact__text">1 888 LIFT HAULS</span>
      </li>
      <li class="contact__item">
        <span class="contact__icon"><svg viewBox="0 0 12 12"><rect x="1" y="2.5" width="10" height="7" fill="none" stroke="#fff" stroke-width="1.2"/><path d="M1 2.5 L6 6.5 L11 2.5" fill="none" stroke="#fff" stroke-width="1.2"/></svg></span>
        <span class="contact__text">mark@hlhaulers.com</span>
      </li>
      <li class="contact__item">
        <span class="contact__icon"><svg viewBox="0 0 12 12"><circle cx="6" cy="6" r="4.8" fill="none" stroke="#fff" stroke-width="1.1"/><ellipse cx="6" cy="6" rx="2.2" ry="4.8" fill="none" stroke="#fff" stroke-width="1"/><path d="M1.2 6 H10.8 M2 3.6 H10 M2 8.4 H10" stroke="#fff" stroke-width=".9"/></svg></span>
        <span class="contact__text">www.<span class="contact__hl">hlhaulers</span>.com</span>
      </li>
    </ul>
    <p class="contact__address">428 Westcott Ave<br>Merrick, NY 11542</p>
  </div>
</section>

</body>
</html>
```